Property Management Company Website

I need a complete website for a property management company in Texas. Our current site (www.brennoakrealtyandmanagement.com) needs to be revamped. My goal is to have a design that appeals more toward residential real estate investors rather than tenants. I would like the site to be more clean and business like. There is a lot of good content on the site that can be used; information about the company, services, etc. The main contact that focuses on real estate investors can be found on the investors and management tabs.

A sample site that I like can be found at: www.pelmarveholdings.com. I like it because it's clean, professional and easy to use. Hopefull this helps as a guide. I however, want this site to be unique.

I have NetPavo hosting services and also cloverbay hosting services already set up.

I also want to make sure that we include links to our social media:
-Twitter - @brennoakrealtytx
-Facebook - www.facebook.com/brennoakrealtyandmanagement
-Youtube - www.youtube.com/BrennoakRealtyTX

Message me if you need any additional photos

Industry/Entity Type

Property Management

```html
<!DOCTYPE html>
<html lang="en">
<head>
<meta charset="utf-8">
<title>Brennoak Realty and Management</title>
<link href="https://fonts.googleapis.com/css2?family=Open+Sans:ital,wght@0,400;0,600;0,700;1,400&display=swap" rel="stylesheet">
<style>
:root{
  --purple:#5a2a82;
  --purple-dark:#45206a;
  --beige:#efe9dc;
  --beige-dark:#e2d9c5;
  --text:#555;
  --muted:#888;
  --line:#ddd;
  --panel:#f3f3f3;
  --white:#fff;
}
*{box-sizing:border-box;margin:0;padding:0}
html,body{width:853px;height:1200px;overflow:hidden}
body{font-family:"Open Sans",Arial,sans-serif;color:var(--text);background:var(--white);font-size:8px;line-height:1.45}
.wrap{width:640px;margin:0 auto;position:relative}
.site-header{height:94px;background:linear-gradient(#fff,var(--beige))}
.site-header .wrap{height:94px}
.brand{position:absolute;left:0;top:14px}
.brand-name{display:flex;align-items:center;gap:6px;font-size:26px;font-weight:600;color:var(--purple);line-height:1}
.brand-name i{width:10px;height:10px;background:var(--purple);display:block}
.brand-tag{font-style:italic;font-size:9px;color:var(--purple);margin:4px 0 0 18px}
.contact{position:absolute;right:0;top:16px;text-align:right;font-size:8px;color:var(--muted)}
.contact div{display:flex;align-items:center;justify-content:flex-end;gap:5px;margin-bottom:4px}
.contact svg{width:10px;height:10px;fill:var(--purple)}
.main-nav{background:var(--purple);height:34px;display:flex;justify-content:space-between;align-items:center;padding:0 14px}
.main-nav a{color:#fff;text-decoration:none;font-size:8px;font-weight:600;letter-spacing:.3px;padding:0 6px;line-height:34px}
.main-nav a.active{background:var(--purple-dark)}
.hero{height:296px;margin-top:8px;position:relative;background:linear-gradient(#b9cfe6 0%,#dfe7ee 35%,#a99a86 60%,#6f7d58 100%)}
.hero-caption{position:absolute;left:32px;top:186px;width:232px;background:rgba(0,0,0,.55);color:#fff;padding:10px 12px}
.hero-caption h2{font-size:15px;font-weight:400;margin-bottom:4px}
.hero-caption p{font-size:7.5px}
.dots{position:absolute;left:50%;bottom:10px;transform:translateX(-50%);display:flex;gap:4px}
.dots span{width:6px;height:6px;border-radius:50%;background:#fff;opacity:.6}
.dots span.on{opacity:1;background:var(--purple)}
.services{display:flex;gap:6px;margin-top:6px;height:112px}
.service{flex:1;background:var(--panel);border-top:3px solid var(--line);padding:8px 10px}
.service h3{font-size:10px;font-weight:600;color:#666;text-transform:uppercase;margin-bottom:5px}
.service p{font-size:7px;color:var(--muted);margin-bottom:6px}
.service a{color:var(--purple);font-size:7px;text-decoration:underline;display:block}
.service small{font-size:6.5px;color:var(--muted)}
.welcome{text-align:center;margin-top:14px}
.welcome h1{color:var(--purple);font-size:13px;font-weight:600;text-transform:uppercase}
.welcome .slogan{color:var(--purple);font-size:9px;font-style:italic;margin:2px 0 4px}
.welcome p{font-size:7px;color:var(--muted);padding:0 18px}
.section-title{text-align:center;color:var(--purple);font-size:13px;font-weight:600;text-transform:uppercase;margin-top:14px;margin-bottom:10px}
.featured{display:flex;gap:16px;padding:0 20px;height:156px}
.feat-card{flex:1;display:flex;gap:8px;border:1px solid var(--line);padding:8px;position:relative}
.feat-photo{width:120px;height:94px;background:linear-gradient(#b9cde0,#c7b9a3 55%,#6d7f52)}
.badge{position:absolute;left:14px;top:96px;width:36px;height:36px;border-radius:50%;background:var(--purple)}
.feat-info h4{font-size:8px;color:var(--purple);font-weight:600}
.feat-info h5{font-size:7px;color:#666;font-weight:600;margin-bottom:4px}
.feat-info p{font-size:6.8px;color:var(--muted);margin-bottom:4px}
.feat-info a{font-size:7px;color:var(--purple)}
.meta{display:grid;grid-template-columns:1fr 1fr;gap:3px;margin-top:6px;font-size:6.5px;color:var(--muted)}
.meta span{display:flex;align-items:center;gap:3px}
.meta span::before{content:"";width:7px;height:7px;border:1px solid #aaa;display:block}
.luxury{display:flex;gap:8px;height:160px}
.lux-card{flex:1;border:1px solid var(--line)}
.lux-photo{height:88px;background:linear-gradient(#bfd2e4,#cbbfae 55%,#6b7b55)}
.lux-body{padding:5px 7px}
.lux-body h4{font-size:8px;color:#666;font-weight:600}
.lux-body p{font-size:6.5px;color:var(--muted)}
.price{font-size:9px;color:var(--purple);font-weight:700;margin-top:3px}
.price small{font-weight:400;color:var(--muted);font-size:6.5px}
.lux-meta{display:flex;gap:10px;font-size:6.5px;color:var(--muted);border-top:1px solid var(--line);margin-top:4px;padding-top:3px}
.site-footer{position:absolute;left:0;top:1094px;width:853px;height:106px;background:linear-gradient(var(--beige),var(--beige-dark))}
.site-footer .wrap{height:106px}
.foot-brand{position:absolute;left:0;top:20px;display:flex;align-items:center;gap:5px;font-size:20px;font-weight:600;color:var(--purple)}
.foot-brand i{width:8px;height:8px;background:var(--purple);display:block}
.foot-links{position:absolute;left:150px;top:28px;font-size:7px;color:#777}
.foot-links a{color:#777;text-decoration:none;margin-right:6px}
.copy{position:absolute;left:150px;top:44px;font-size:6.5px;color:var(--muted)}
.social{position:absolute;right:0;top:24px;display:flex;gap:4px}
.social span{width:16px;height:16px;background:var(--purple)}
</style>
</head>
<body>
<header class="site-header">
  <div class="wrap">
    <div class="brand">
      <div class="brand-name"><i></i>Brennoak</div>
      <div class="brand-tag">"Committed To Success!"</div>
    </div>
    <div class="contact">
      <div>(972) 555-0148 <svg viewBox="0 0 24 24"><path d="M6.6 10.8a15 15 0 0 0 6.6 6.6l2.2-2.2c.3-.3.7-.4 1-.2 1.1.4 2.3.6 3.6.6.6 0 1 .4 1 1V20c0 .6-.4 1-1 1A17 17 0 0 1 3 4c0-.6.4-1 1-1h3.5c.6 0 1 .4 1 1 0 1.3.2 2.5.6 3.6.1.3 0 .7-.2 1z"/></svg></div>
      <div>info@brennoakrealty.com <svg viewBox="0 0 24 24"><path d="M2 5h20v14H2zm2 2v.5l8 5 8-5V7z"/></svg></div>
    </div>
  </div>
</header>

<div class="wrap">
  <nav class="main-nav">
    <a class="active" href="#">HOME</a><a href="#">ABOUT US</a><a href="#">CAREERS</a><a href="#">BUYERS</a><a href="#">SELLERS</a><a href="#">INVESTORS</a><a href="#">MANAGEMENT</a><a href="#">LEASING</a><a href="#">CONTACT US</a>
  </nav>

  <section class="hero" role="img" aria-label="Photo of a large two-storey stone luxury home with trees and lawn">
    <div class="hero-caption">
      <h2>Luxury Homes</h2>
      <p>Lorem ipsum dolor sit amet, consectetur adipiscing elit, sed diam nonummy.</p>
    </div>
    <div class="dots"><span class="on"></span><span></span><span></span></div>
  </section>

  <section class="services">
    <div class="service">
      <h3>Sellers</h3>
      <p>They say it's a buyer's market! Let us help you make your property stand out from the competition.</p>
      <a href="#">Visit above</a><small>A Seller's Guide to Success</small>
    </div>
    <div class="service">
      <h3>Buyers</h3>
      <p>The housing market has reached the bottom! Don't hesitate, and begin your search today.</p>
      <a href="#">Visit above</a><small>A Buyer's Guide to Success</small>
    </div>
    <div class="service">
      <h3>Management</h3>
      <p>The alternative key to success with any real estate investment portfolio is competent management.</p>
      <a href="#">Visit above</a><small>A Seller's Guide to Success</small>
    </div>
  </section>

  <section class="welcome">
    <h1>Welcome to Brennoak Realty and Management</h1>
    <div class="slogan">"Committed to Success!"</div>
    <p>Nam liber tempor cum soluta nobis eleifend option congue nihil imperdiet doming id quod mazim placerat facer possim assum. Typi non habent claritatem insitam; est usus legentis in iis qui facit eorum claritatem. Investigationes demonstraverunt lectores legere me lius quod ii legunt saepius.</p>
  </section>

  <h2 class="section-title">Featured Listings</h2>
  <section class="featured">
    <article class="feat-card">
      <div class="feat-photo" role="img" aria-label="Photo of a brick family home with a front lawn"></div>
      <span class="badge"></span>
      <div class="feat-info">
        <h4>218 Cedar Ridge Lane</h4>
        <h5>Irving, TEXAS 75063</h5>
        <p>Lorem ipsum dolor sit amet, consectetur adipiscing elit, sed diam nonummy euismod tincidunt.</p>
        <a href="#">Learn more</a>
        <div class="meta"><span>2,400 sqft</span><span>4 Beds</span><span>3 Baths</span><span>Garage</span></div>
      </div>
    </article>
    <article class="feat-card">
      <div class="feat-photo" role="img" aria-label="Photo of a stone family home with a front lawn"></div>
      <span class="badge"></span>
      <div class="feat-info">
        <h4>218 Cedar Ridge Lane</h4>
        <h5>Irving, TEXAS 75063</h5>
        <p>Lorem ipsum dolor sit amet, consectetur adipiscing elit, sed diam nonummy euismod tincidunt.</p>
        <a href="#">Learn more</a>
        <div class="meta"><span>2,400 sqft</span><span>4 Beds</span><span>3 Baths</span><span>Garage</span></div>
      </div>
    </article>
  </section>

  <h2 class="section-title">Luxury Listings</h2>
  <section class="luxury">
    <article class="lux-card"><div class="lux-photo" role="img" aria-label="Photo of a luxury brick house"></div><div class="lux-body"><h4>Lorem ipsum</h4><p>Nam liber tempor cum soluta</p><div class="price">$ 250.00 <small>sq.ft</small></div><div class="lux-meta"><span>3 Beds</span><span>2 Baths</span></div></div></article>
    <article class="lux-card"><div class="lux-photo" role="img" aria-label="Photo of a luxury stone house"></div><div class="lux-body"><h4>Lorem ipsum</h4><p>Nam liber tempor cum soluta</p><div class="price">$ 250.00 <small>sq.ft</small></div><div class="lux-meta"><span>3 Beds</span><span>2 Baths</span></div></div></article>
    <article class="lux-card"><div class="lux-photo" role="img" aria-label="Photo of a luxury house with trees"></div><div class="lux-body"><h4>Lorem ipsum</h4><p>Nam liber tempor cum soluta</p><div class="price">$ 250.00 <small>sq.ft</small></div><div class="lux-meta"><span>3 Beds</span><span>2 Baths</span></div></div></article>
    <article class="lux-card"><div class="lux-photo" role="img" aria-label="Photo of a large white luxury house"></div><div class="lux-body"><h4>Lorem ipsum</h4><p>Nam liber tempor cum soluta</p><div class="price">$ 250.00 <small>sq.ft</small></div><div class="lux-meta"><span>3 Beds</span><span>2 Baths</span></div></div></article>
  </section>
</div>

<footer class="site-footer">
  <div class="wrap">
    <div class="foot-brand"><i></i>Brennoak</div>
    <div class="foot-links"><a href="#">Privacy Policy</a>| <a href="#">Terms &amp; conditions</a>| <a href="#">Sitemap</a>| <a href="#">Contact</a></div>
    <div class="copy">Copyright © Brennoak Realty and Management. All rights reserved.</div>
    <div class="social" aria-label="Social media links"><span></span><span></span><span></span><span></span><span></span></div>
  </div>
</footer>
</body>
</html>
```